"ZENTRAL BEAT" - German Rap Concert

Hello,

I need a Flyer for a concert in Reutlingen, Germany.
The following Information should be included in the Flyer:

"ZENTRAL BEAT

09.01.2015
Beginn: 17:00 Uhr
Einlass: 15:30 Uhr

Acts:
OLU BRANDT
Mira Quell
Rotfeld & SolarBoy
RUV
Salihu. PNW & Luppo
TwoStep

VVK: 26€

Klangwerk, Lindenweg 14, 72760 Reutlingen"

The Logo of the Location should also be in the Flyer.
Main Act is Olu Brandt. you can find a Picture of him attached.
We also need space for Sponsoring-logos (4) at the bottom of the Flyer.
The Logos of the Sponsors will come later.

I hope you can understand my english ;)
If you have any questions, just write me an email.

Thanks in advance!

Tobias

Edit: The size of the Flyer should be DinA6.
I have also uploaded a better Version of the Klangwerk Logo!
Updates

Dear Designers, I have uploaded 3 of the 4 Sponsoring-Logos. Please insert them into the Flyer! Sponsors: LDR-S (please write under the logo "Sport- & Eventmanagement") Moos Brauerei Wendlinger Thanks!

```html
<!DOCTYPE html>
<html lang="de">
<head>
<meta charset="utf-8">
<title>Zentral Beat – Flyer</title>
<link rel="stylesheet" href="https://fonts.googleapis.com/css2?family=Oswald:wght@300;400;600;700&family=Roboto:wght@400;700&display=swap">
<style>
  :root {
    --stage: #4f4f4f;
    --flyer-red: #c7434f;
    --photo-light: #e08a8f;
    --photo-dark: #8e2633;
    --panel-red: rgba(150, 32, 46, 0.86);
    --strip-red: #9c2a38;
    --accent-yellow: #f4e31c;
    --paper: #f7f4f3;
    --ink: #1e1e1e;
    --white: #ffffff;
    --navy: #1d2f6b;
  }
  * { margin: 0; padding: 0; box-sizing: border-box; }
  html, body {
    width: 1200px; height: 900px; overflow: hidden;
    background: var(--stage);
  }
  .flyer {
    position: absolute; left: 301px; top: 27px;
    width: 598px; height: 846px;
    background: var(--flyer-red);
    overflow: hidden;
    font-family: "Oswald", "Arial Narrow", sans-serif;
    color: var(--white);
  }
  .artist-photo {
    position: absolute; inset: 0 0 120px 0;
    background:
      radial-gradient(ellipse 38% 46% at 52% 34%, var(--photo-light), transparent 70%),
      linear-gradient(160deg, var(--flyer-red) 0%, var(--photo-dark) 100%);
  }
  .venue-logo {
    position: absolute; right: 30px; top: 30px;
    display: flex; align-items: center; gap: 8px;
    font-weight: 700; font-size: 30px; letter-spacing: 1px;
    color: var(--white);
  }
  .venue-logo .mark { width: 14px; height: 14px; background: var(--white); }
  .info-panel {
    position: absolute; left: 0; top: 355px;
    width: 275px; height: 335px;
    background: var(--panel-red);
    padding: 26px 28px;
  }
  .event-title { font-weight: 600; font-size: 24px; line-height: 1.1; letter-spacing: .3px; }
  .event-times { font-weight: 300; font-size: 16px; line-height: 1.35; margin-top: 6px; }
  .acts-label { color: var(--accent-yellow); font-weight: 600; font-size: 17px; margin-top: 22px; }
  .act-list { list-style: none; font-weight: 300; font-size: 16px; line-height: 1.32; }
  .act-list .headliner { color: var(--accent-yellow); font-weight: 600; }
  .presale { color: var(--accent-yellow); font-weight: 700; font-size: 30px; margin-top: 14px; }
  .sponsor-band {
    position: absolute; left: 0; right: 0; top: 718px; height: 72px;
    background: var(--paper);
    display: flex; align-items: center; justify-content: space-between;
    padding: 0 18px 0 24px;
  }
  .sponsor-placeholder { font-family: "Roboto", Arial, sans-serif; font-size: 15px; color: var(--ink); }
  .sponsor-logos { display: flex; align-items: center; gap: 16px; }
  .sponsor {
    display: flex; align-items: center; gap: 6px;
    font-family: "Oswald", sans-serif; font-weight: 600; font-size: 15px;
    color: var(--navy);
  }
  .sponsor .dot { width: 10px; height: 10px; border-radius: 50%; background: var(--navy); }
  .sponsor-stack { display: flex; flex-direction: column; align-items: center; }
  .sponsor-stack small { font-family: "Roboto", sans-serif; font-size: 8px; color: var(--ink); }
  .credit-strip {
    position: absolute; left: 0; right: 0; top: 790px; bottom: 0;
    background: var(--strip-red);
    display: flex; align-items: center; justify-content: flex-end;
    padding: 0 26px;
    font-family: "Roboto", Arial, sans-serif; font-size: 13px; color: var(--white);
  }
</style>
</head>
<body>
  <main class="flyer">
    <div class="artist-photo" role="img" aria-label="Duotone portrait of headliner Olu Brandt wearing sunglasses, in light and dark red tones"></div>

    <div class="venue-logo"><span class="mark"></span>KLANGWERK</div>

    <section class="info-panel">
      <h1 class="event-title">ZENTRAL BEAT</h1>
      <p class="event-times">09.01.2015<br>Beginn: 17:00 Uhr<br>Einlass: 15:30 Uhr</p>
      <p class="acts-label">Acts:</p>
      <ul class="act-list">
        <li class="headliner">OLU BRANDT</li>
        <li>Mira Quell</li>
        <li>Rotfeld &amp; SolarBoy</li>
        <li>RUV</li>
        <li>Salihu. PNW &amp; Luppo</li>
        <li>TwoStep</li>
      </ul>
      <p class="presale">VVK: 26€</p>
    </section>

    <section class="sponsor-band">
      <span class="sponsor-placeholder">Sponsoring-logos Here</span>
      <div class="sponsor-logos">
        <span class="sponsor"><span class="dot"></span>Wendlinger</span>
        <span class="sponsor-stack"><span class="sponsor">LDR-S</span><small>Sport- &amp; Eventmanagement</small></span>
        <span class="sponsor">Moos Brauerei</span>
      </div>
    </section>

    <footer class="credit-strip">Sport- &amp; Eventmanagement" Moos Brauerei Wendlinger</footer>
  </main>
</body>
</html>
```